Water Filter Company Needs Bizz Cards!!

Need business cards for my company. We sell whole home water filters and salt free water softeners. No more buying bottled water. Our filtering units filter out all heavy metals, chlorine, and VOC's, last 15 years, and are maintenance free and supply your whole home with spring quality alkaline water. Our Salt free water conditioners, eliminate hard water and scale, without lowering the ph, or TDS's (total Dissolved solids)

I think this is the color code we are using on my site. My logo looks good behind it. #192841

Website will be www.Brovexa.com

Industry/Entity Type

Water Purification

Contact Information for Business Card

For now, just insert standard Dummy text. I need these text lines for the info to be editable so i can make them for multiple employees. I do have Photoshop and illustrator, unless there is a simpler program i can use solely for biz cards

Font styles to use
Sans Serif

Requirements
Must have
• Use my preexisting logo.

www.BroVexa.com

Spring Quality Alkaline Water at every tap.

List out services. Whole Home Water Filters, Salt Free Water Softeners, Clarimont KT7, UV Sterilizers
Nice to have
• I think this is the color code we are using on my site. My logo looks good behind it. #192841 or black. Please no white or light blue backgrounds.

Maybe a picture of my tank.

Slogan like Spring Quality Alkaline Water at every tap.
And just list the services Whole Home Water Filters, Salt Free Water Softeners, Clarimont KT7, UV Sterilizers

I think I would like to not have a contrasting textured logo like I see on some of them. I may use it for my personal cards, but new employees may not want the extra expense.
Should not have
• A different logo than the one provided.

White or baby blue backgrounds. Use the color code, or blacks.

```html
<!DOCTYPE html>
<html lang="en">
<head>
<meta charset="utf-8">
<title>Brovexa Business Cards</title>
<link rel="stylesheet" href="https://fonts.googleapis.com/css2?family=Comfortaa:wght@400;600&family=Montserrat:wght@400;500;700&family=Oswald:wght@300;400&display=swap">
<style>
  :root {
    --page-bg: #e4e8ee;
    --card-bg: #0b0b0c;
    --card-bg-edge: #1a1a1c;
    --accent: #3aaee0;
    --text-light: #f2f2f2;
    --text-soft: #cfcfcf;
    --rule-grey: #d9d9d9;
  }
  * { box-sizing: border-box; margin: 0; padding: 0; }
  html, body { width: 1200px; height: 675px; overflow: hidden; }
  body {
    background: var(--page-bg);
    font-family: "Montserrat", sans-serif;
    color: var(--text-light);
    position: relative;
  }
  .card {
    position: absolute;
    top: 183px;
    width: 540px;
    height: 309px;
    background: linear-gradient(160deg, var(--card-bg-edge), var(--card-bg) 55%);
    border-radius: 4px;
    overflow: hidden;
    box-shadow: 0 10px 30px rgba(20, 30, 50, 0.25);
  }
  .card--front { left: 40px; }
  .card--back { left: 620px; }

  /* Front */
  .brand {
    display: flex;
    align-items: center;
    gap: 10px;
    font-family: "Montserrat", sans-serif;
    font-weight: 700;
    color: var(--accent);
  }
  .brand__dot {
    border-radius: 50%;
    background: var(--accent);
  }
  .card--front .brand {
    position: absolute;
    left: 0; right: 0; top: 92px;
    justify-content: center;
    font-size: 50px;
    letter-spacing: -0.5px;
  }
  .card--front .brand__dot { width: 34px; height: 34px; }
  .slogan {
    position: absolute;
    left: 0; right: 0; bottom: 58px;
    text-align: center;
    font-family: "Comfortaa", sans-serif;
    font-size: 15px;
    color: var(--text-soft);
    letter-spacing: 0.3px;
  }

  /* Back */
  .card--back .brand {
    position: absolute;
    right: 34px; top: 24px;
    font-size: 24px;
    gap: 6px;
  }
  .card--back .brand__dot { width: 16px; height: 16px; }
  .product-photo {
    position: absolute;
    right: 60px; top: 64px;
    width: 150px; height: 92px;
    border-radius: 4px;
    background: linear-gradient(90deg, #9a9ea3 0%, #d9d6bf 45%, #2b2b2e 75%, #1b1b1d 100%);
  }
  .services {
    position: absolute;
    right: 30px; top: 172px;
    list-style: none;
    text-align: right;
    font-size: 12.5px;
    line-height: 17px;
    color: var(--text-light);
    text-transform: uppercase;
  }
  .services li::after {
    content: "";
    display: inline-block;
    width: 5px; height: 5px;
    border-radius: 50%;
    background: var(--text-light);
    margin-left: 7px;
    vertical-align: middle;
  }
  .person {
    position: absolute;
    left: 36px; top: 96px;
  }
  .person__name {
    font-family: "Oswald", sans-serif;
    font-weight: 300;
    font-size: 32px;
    letter-spacing: 7px;
    color: var(--accent);
    line-height: 1;
  }
  .person__name span { color: var(--text-light); }
  .person__role {
    margin-top: 6px;
    font-size: 12px;
    letter-spacing: 9px;
    color: var(--text-light);
  }
  .person__rule {
    margin-top: 8px;
    width: 58px; height: 3px;
    background: var(--accent);
  }
  .contacts {
    position: absolute;
    left: 36px; top: 178px;
    list-style: none;
    font-size: 14px;
    line-height: 19px;
  }
  .contacts li {
    display: flex;
    align-items: flex-start;
    gap: 12px;
    margin-bottom: 3px;
  }
  .contacts svg { flex: none; width: 13px; height: 13px; margin-top: 3px; fill: var(--text-soft); }
  .bottom-bar {
    position: absolute;
    left: 270px; right: 0; bottom: 0;
    height: 6px;
    display: flex;
  }
  .bottom-bar__accent { flex: 0 0 62%; background: var(--accent); }
  .bottom-bar__grey { flex: 1; background: var(--rule-grey); }
</style>
</head>
<body>

<section class="card card--front">
  <div class="brand"><span class="brand__dot"></span>Brovexa</div>
  <p class="slogan">Spring Quality Alkaline Water at every tap</p>
</section>

<section class="card card--back">
  <div class="brand"><span class="brand__dot"></span>Brovexa</div>
  <div class="product-photo" role="img" aria-label="Photo of the water filter tanks and UV sterilizer"></div>
  <ul class="services">
    <li>Whole Home Water Filters</li>
    <li>Salt Free Water Softeners</li>
    <li>Clarimont KT7</li>
    <li>UV Sterilizers</li>
  </ul>

  <div class="person">
    <h1 class="person__name">JOHN <span>SMITH</span></h1>
    <p class="person__role">POSITION</p>
    <div class="person__rule"></div>
  </div>

  <ul class="contacts">
    <li>
      <svg viewBox="0 0 24 24" aria-hidden="true"><path d="M6.6 10.8a15.1 15.1 0 0 0 6.6 6.6l2.2-2.2a1 1 0 0 1 1-.25 11.4 11.4 0 0 0 3.6.57 1 1 0 0 1 1 1V20a1 1 0 0 1-1 1A17 17 0 0 1 3 4a1 1 0 0 1 1-1h3.5a1 1 0 0 1 1 1c0 1.25.2 2.45.57 3.57a1 1 0 0 1-.25 1z"/></svg>
      <span>+00 000 000 00<br>+00 000 000 00</span>
    </li>
    <li>
      <svg viewBox="0 0 24 24" aria-hidden="true"><path d="M2 5h20v14H2z M4 7v.4l8 5 8-5V7l-8 5z" fill-rule="evenodd"/></svg>
      <span>info@brovexa.com</span>
    </li>
    <li>
      <svg viewBox="0 0 24 24" aria-hidden="true"><path d="M12 2a10 10 0 1 0 0 20 10 10 0 0 0 0-20zm0 2c.9 1.2 1.6 2.6 2 4h-4c.4-1.4 1.1-2.8 2-4zM4.3 14a8 8 0 0 1 0-4h3.4a16 16 0 0 0 0 4zm.9 2h3c.3 1.3.8 2.5 1.4 3.6A8 8 0 0 1 5.2 16zm3-8h-3a8 8 0 0 1 4.4-3.6C8.9 5.5 8.5 6.7 8.2 8zM12 20c-.9-1.2-1.6-2.6-2-4h4c-.4 1.4-1.1 2.8-2 4zm2.3-6H9.7a14 14 0 0 1 0-4h4.6a14 14 0 0 1 0 4zm.1 5.6c.6-1.1 1.1-2.3 1.4-3.6h3a8 8 0 0 1-4.4 3.6zm2-5.6a16 16 0 0 0 0-4h3.4a8 8 0 0 1 0 4z"/></svg>
      <span>www.brovexa.com</span>
    </li>
    <li>
      <svg viewBox="0 0 24 24" aria-hidden="true"><path d="M12 2a7 7 0 0 0-7 7c0 5.2 7 13 7 13s7-7.8 7-13a7 7 0 0 0-7-7zm0 9.5A2.5 2.5 0 1 1 12 6.5a2.5 2.5 0 0 1 0 5z"/></svg>
      <span>address line here, City,<br>State, Country</span>
    </li>
  </ul>

  <div class="bottom-bar">
    <div class="bottom-bar__accent"></div>
    <div class="bottom-bar__grey"></div>
  </div>
</section>

</body>
</html>
```